Stainless Steel Business Card

I have a fiber laser and want to highlight its capabilities in a business card. On the card I want

Brevik Industries
Martin Brevik
martin@mbrevik-mail.net
417-555-0163

This will be cut / engraved on stainless steel. I want the Brevik Industries to be prominent with laser cut font so that there are no dropouts on the O and A's. My name email and phone number should be engraved black. I would like some cool geometric patterns to cutout on the card to highlight the capabilities of my machine. I will need to files in the end either SVG or dxf of the engrave portion and the cut portion.

```html
<!DOCTYPE html>
<html lang="en">
<head>
<meta charset="utf-8">
<title>Brevik Industries – Stainless Steel Business Card</title>
<link rel="stylesheet" href="https://fonts.googleapis.com/css2?family=Saira+Stencil+One&family=Arimo:wght@600;700&display=swap">
<style>
  :root {
    --page-bg: #ffffff;
    --steel-light: #d2d2d2;
    --steel-mid: #c2c2c2;
    --steel-dark: #b3b3b3;
    --cut-through: #ffffff;
    --cut-shadow: #5a5a5a;
    --engrave-black: #111111;
    --card-edge: #a4a4a4;
  }
  html, body {
    margin: 0;
    padding: 0;
    width: 1200px;
    height: 800px;
    overflow: hidden;
    background: var(--page-bg);
  }
  .business-card {
    display: block;
    width: 1200px;
    height: 800px;
  }
  .card-plate { stroke: var(--card-edge); stroke-width: 1.5; }
  .geometric-cut { fill: var(--cut-shadow); }
  .company-name {
    font-family: "Saira Stencil One", "Stardos Stencil", sans-serif;
    fill: var(--cut-through);
    stroke: #8a8a8a;
    stroke-width: 1.2;
  }
  .company-division {
    font-family: "Saira Stencil One", "Stardos Stencil", sans-serif;
    fill: var(--cut-shadow);
  }
  .contact-name {
    font-family: "Arimo", Arial, sans-serif;
    font-weight: 700;
    font-size: 36px;
    fill: var(--engrave-black);
  }
  .contact-detail {
    font-family: "Arimo", Arial, sans-serif;
    font-weight: 600;
    font-size: 31px;
    fill: var(--engrave-black);
  }
</style>
</head>
<body>
<svg class="business-card" viewBox="0 0 1200 800" xmlns="http://www.w3.org/2000/svg" role="img" aria-label="Brevik Industries stainless steel business card">
  <defs>
    <linearGradient id="steelFinish" x1="0" y1="0" x2="1" y2="1">
      <stop offset="0" stop-color="var(--steel-light)"/>
      <stop offset="0.5" stop-color="var(--steel-mid)"/>
      <stop offset="1" stop-color="var(--steel-dark)"/>
    </linearGradient>
    <pattern id="brushedGrain" width="400" height="4" patternUnits="userSpaceOnUse">
      <rect width="400" height="1" fill="#ffffff" opacity="0.12"/>
      <rect y="2" width="400" height="1" fill="#000000" opacity="0.04"/>
    </pattern>
  </defs>

  <!-- Card plate -->
  <rect class="card-plate" x="33" y="56" width="1133" height="706" rx="24" fill="url(#steelFinish)"/>
  <rect x="33" y="56" width="1133" height="706" rx="24" fill="url(#brushedGrain)"/>

  <!-- Geometric cut-outs: top left -->
  <g class="geometric-cut">
    <polygon points="55,238 222,70 255,70 55,271"/>
    <polygon points="212,152 297,70 328,70 243,152"/>
    <polygon points="282,152 367,70 398,70 313,152"/>
  </g>

  <!-- Geometric cut-outs: bottom right -->
  <g class="geometric-cut">
    <polygon points="680,734 836,578 870,578 714,734"/>
    <polygon points="762,734 918,578 952,578 796,734"/>
    <polygon points="846,734 1147,433 1147,467 880,734"/>
    <polygon points="930,734 1147,517 1147,551 964,734"/>
  </g>

  <!-- Company name, laser cut -->
  <text class="company-name" x="137" y="400" font-size="300" textLength="975" lengthAdjust="spacingAndGlyphs">BREVIK</text>
  <text class="company-division" x="139" y="510" font-size="106" textLength="911" lengthAdjust="spacingAndGlyphs">INDUSTRIES</text>

  <!-- Engraved contact details -->
  <text class="contact-name" x="148" y="585">Martin Brevik</text>
  <text class="contact-detail" x="148" y="636">martin@mbrevik-mail.net</text>
  <text class="contact-detail" x="148" y="687">417-555-0163</text>
</svg>
</body>
</html>
```